Quorvex business card design

create modern and tech looking business card that is clean but effectively communciates that we are a cloud communications company.
Should have at minimum:
Employee Name
Postion
Phone Number
Email
website
create modern and tech looking business card that is clean but effectively communciates that we are a cloud communications company. We have two logo color schemes (attached) so would like to see designs both ways
Should have at minimum:
Employee Name
Postion
Phone Number
Email
website

```html
<!DOCTYPE html>
<html lang="en">
<head>
<meta charset="utf-8">
<title>Quorvex business card</title>
<link href="https://fonts.googleapis.com/css2?family=Oswald:wght@500&family=Open+Sans:wght@400;600&display=swap" rel="stylesheet">
<style>
  :root {
    --bg: #8f8f91;
    --card: #e6e6e9;
    --brand-blue: #1a97c6;
    --brand-purple: #4b2a80;
    --ink: #3a3a40;
    --muted: #55555c;
    --rule: #55555c;
  }
  * { margin: 0; padding: 0; box-sizing: border-box; }
  html, body { width: 1200px; height: 781px; overflow: hidden; }
  body { background: var(--bg); position: relative; font-family: "Open Sans", sans-serif; }
  .card {
    position: absolute;
    left: 358px;
    width: 452px;
    height: 250px;
    background: var(--card);
    box-shadow: 0 6px 10px rgba(0,0,0,0.25);
  }
  .card--front { top: 104px; }
  .card--back { top: 408px; }

  .identity {
    position: absolute;
    right: 243px;
    top: 102px;
    text-align: right;
  }
  .identity__name {
    font-family: "Oswald", sans-serif;
    font-weight: 500;
    font-size: 31px;
    line-height: 1;
    color: var(--brand-blue);
    letter-spacing: -0.3px;
    white-space: nowrap;
  }
  .identity__role {
    font-size: 11px;
    color: var(--muted);
    margin-top: 4px;
  }
  .divider {
    position: absolute;
    left: 223px;
    top: 106px;
    width: 1px;
    height: 44px;
    background: var(--rule);
  }
  .contact {
    position: absolute;
    left: 238px;
    top: 105px;
    list-style: none;
  }
  .contact__item {
    display: flex;
    align-items: center;
    gap: 7px;
    font-size: 10.5px;
    line-height: 15px;
    color: var(--ink);
    white-space: nowrap;
  }
  .contact__icon { width: 9px; height: 9px; flex: none; }

  .wordmark {
    position: absolute;
    left: 0; right: 0;
    top: 112px;
    display: flex;
    justify-content: center;
    align-items: center;
    gap: 9px;
  }
  .wordmark__mark { width: 14px; height: 14px; background: var(--brand-blue); }
  .wordmark__name {
    font-weight: 600;
    font-size: 22px;
    letter-spacing: 1px;
    color: var(--brand-purple);
  }
</style>
</head>
<body>
  <section class="card card--front">
    <div class="identity">
      <div class="identity__name">MARK WELLS</div>
      <div class="identity__role">Manager</div>
    </div>
    <div class="divider"></div>
    <ul class="contact">
      <li class="contact__item">
        <svg class="contact__icon" viewBox="0 0 10 10"><path d="M2 0.8 L3.6 0.8 L4.2 3 L3 3.8 Q4 6 6.2 7 L7 5.8 L9.2 6.4 L9.2 8 Q9 9.2 7.8 9.2 Q1 8.5 0.8 2.2 Q0.8 0.8 2 0.8Z" fill="var(--brand-purple)"/></svg>
        +555 0148 2390
      </li>
      <li class="contact__item">
        <svg class="contact__icon" viewBox="0 0 10 10"><rect x="0.5" y="2" width="9" height="6.5" fill="var(--brand-purple)"/><path d="M0.8 2.3 L5 5.6 L9.2 2.3" stroke="#fff" stroke-width="0.9" fill="none"/></svg>
        hello@quorvex.com
      </li>
      <li class="contact__item">
        <svg class="contact__icon" viewBox="0 0 10 10"><circle cx="5" cy="5" r="4.4" fill="none" stroke="var(--brand-purple)" stroke-width="1"/><ellipse cx="5" cy="5" rx="1.8" ry="4.4" fill="none" stroke="var(--brand-purple)" stroke-width="0.8"/><path d="M0.8 5 H9.2" stroke="var(--brand-purple)" stroke-width="0.8"/></svg>
        www.quorvex.com
      </li>
    </ul>
  </section>

  <section class="card card--back">
    <div class="wordmark">
      <span class="wordmark__mark"></span>
      <span class="wordmark__name">QUORVEX</span>
    </div>
  </section>
</body>
</html>
```